Ablaufgrafik KlickWerkstatt
Zielgruppe
KlickWerkstatt: Content Marketing-Lösung für KMU
Ohne Aufwand verleiht KlickWerkstatt Inhalten (Produkt-Meldungen, Presse-Mitteilungen, Blog-Artikel, …) die notwendige Reichweite um Neukundenkontakte zu generieren.
Der Content geht über alle Kanäle: Web, Mail und Social.
Der KlickWerkstatt bietet flexible und maßgeschneiderte Online Marketing Lösungen, die sich am Bedarf hinsichtlich Quantität, Qualität, den Kunden-Bedürfnissen und dem Budget angleichen. Bis hin zu individuell selektierten Verteilern.
Aufgabenstellung
Es soll eine Ablaufgrafik erstellt werden, die visualisiert "Was passiert mit meinem Content über den KlickWerkstatt": Eine Prozess-Visualisierung.
Die Ablaufgrafik wird als JPG/PNG bei klickwerkstatt.de eingebunden: Mit klick öffnet sich eine bildschirmfüllende Grafik. Ebenso soll die Grafik im factsheet (pdf) eingebunden werden.
- CI gemäß www.klickwerkstatt.de
- Anschauung und Info: factsheet-PDF http://kurzlink-beispiel.de/Rw7TqZ
- Logo: http://kurzlink-beispiel.de/Jm3VbK
Skizze zum Aufbau und den Inhalten für die Ablaufgrafik: s. Dateianlage (pdf)

```html
<!DOCTYPE html>
<html lang="de">
<head>
<meta charset="utf-8">
<title>Ablaufgrafik KlickWerkstatt</title>
<link href="https://fonts.googleapis.com/css2?family=Lato:wght@400;700&display=swap" rel="stylesheet">
<style>
  :root {
    --blue: #56c1df;
    --blue-dark: #3e8fa8;
    --orange: #f28c1e;
    --green: #7dc386;
    --ink: #161616;
    --paper: #ffffff;
    --people: #c9b8a6;
  }
  html, body {
    margin: 0;
    padding: 0;
    width: 1032px;
    height: 1200px;
    overflow: hidden;
    background: var(--paper);
  }
  .flow {
    display: block;
    width: 1032px;
    height: 1200px;
    font-family: "Lato", sans-serif;
  }
  .stage-label { fill: var(--green); }
  .stage-text { fill: #fff; font-size: 33px; font-weight: 700; letter-spacing: .5px; }
  .diamond-edge { fill: #fff; stroke: var(--blue); stroke-width: 1.5; }
  .diamond-base { fill: var(--blue); }
  .diamond-title { fill: var(--ink); font-size: 34px; font-weight: 700; text-anchor: middle; }
  .step-box { fill: #fff; stroke: var(--blue); stroke-width: 1.5; }
  .step-text { fill: var(--ink); font-size: 27px; }
  .connector { fill: none; stroke: var(--orange); stroke-width: 4; stroke-dasharray: 9 7; }
  .pin { fill: var(--green); }
  .pin-text { fill: #fff; font-size: 27px; text-anchor: middle; }
  .pin-base-top { fill: var(--blue); }
  .pin-base-side { fill: #fff; stroke: var(--blue); stroke-width: 1.5; }
  .pin-shadow { fill: var(--blue-dark); }
  .audience-top { fill: var(--blue); }
  .audience-side { fill: #fff; stroke: var(--blue); stroke-width: 1.5; }
  .audience-people { fill: var(--people); }
  .claim { fill: var(--green); font-size: 28px; font-weight: 700; text-anchor: middle; letter-spacing: .5px; }
</style>
</head>
<body>
<svg class="flow" viewBox="0 0 1780 2070" xmlns="http://www.w3.org/2000/svg">
  <defs>
    <linearGradient id="stageFade" x1="0" y1="0" x2="1" y2="0.6">
      <stop offset="0" stop-color="#7dc386" stop-opacity=".45"/>
      <stop offset=".55" stop-color="#7dc386" stop-opacity=".12"/>
      <stop offset="1" stop-color="#7dc386" stop-opacity="0"/>
    </linearGradient>
  </defs>

  <!-- stage bands -->
  <g class="stage">
    <polygon points="38,83 720,83 38,310" fill="url(#stageFade)"/>
    <polygon class="stage-label" points="38,83 340,83 228,150 38,150"/>
    <text class="stage-text" x="52" y="126">ERSTELLEN</text>
  </g>
  <g class="stage">
    <polygon points="38,556 720,556 38,785" fill="url(#stageFade)"/>
    <polygon class="stage-label" points="38,556 340,556 228,623 38,623"/>
    <text class="stage-text" x="52" y="599">VERBREITEN</text>
  </g>
  <g class="stage">
    <polygon points="38,1435 500,1435 38,1770" fill="url(#stageFade)"/>
    <polygon class="stage-label" points="38,1435 340,1435 228,1502 38,1502"/>
    <text class="stage-text" x="52" y="1478">AUSWERTEN</text>
  </g>

  <!-- connectors -->
  <g class="connectors">
    <path class="connector" d="M777,202 L690,255"/>
    <path class="connector" d="M568,324 L495,368"/>
    <path class="connector" d="M947,202 L1032,255"/>
    <path class="connector" d="M1153,324 L1228,368"/>
    <path class="connector" d="M572,436 L758,545"/>
    <path class="connector" d="M1150,436 L963,545"/>
    <path class="connector" d="M763,660 L588,765"/>
    <path class="connector" d="M520,805 L347,905 L347,956"/>
    <path class="connector" d="M861,720 L861,770"/>
    <path class="connector" d="M957,660 L1140,765"/>
    <path class="connector" d="M1203,805 L1375,905"/>
    <path class="connector" d="M347,1024 L347,1080"/>
    <path class="connector" d="M347,1148 L347,1200 L712,1412"/>
    <path class="connector" d="M861,940 L861,1010"/>
    <path class="connector" d="M861,1136 L861,1180"/>
    <path class="connector" d="M861,1248 L861,1291"/>
    <path class="connector" d="M861,1359 L861,1435"/>
    <path class="connector" d="M1375,973 L1375,1019"/>
    <path class="connector" d="M1375,1087 L1375,1131"/>
    <path class="connector" d="M1375,1199 L1010,1412"/>
    <path class="connector" d="M861,1550 L861,1635"/>
  </g>

  <!-- diamond: Ihre News -->
  <g class="diamond">
    <polygon class="diamond-base" points="670,135 861,246 1052,135 1052,150 861,261 670,150"/>
    <polygon class="diamond-edge" points="861,24 1052,135 861,246 670,135"/>
    <text class="diamond-title" x="861" y="147">IHRE NEWS</text>
  </g>

  <!-- create steps -->
  <g class="steps">
    <rect class="step-box" x="520" y="255" width="233" height="68"/>
    <text class="step-text" x="530" y="297">Mail</text>
    <rect class="step-box" x="968" y="255" width="233" height="68"/>
    <text class="step-text" x="978" y="297">Login</text>
    <rect class="step-box" x="397" y="368" width="233" height="68"/>
    <text class="step-text" x="407" y="409">Einstellservice</text>
    <rect class="step-box" x="1085" y="368" width="233" height="68"/>
    <text class="step-text" x="1095" y="409">Redaktionssystem</text>
  </g>

  <!-- diamond: Ihr Newsroom -->
  <g class="diamond">
    <polygon class="diamond-base" points="670,600 861,711 1052,600 1052,615 861,726 670,615"/>
    <polygon class="diamond-edge" points="861,489 1052,600 861,711 670,600"/>
    <text class="diamond-title" x="861" y="612">IHR NEWSROOM</text>
  </g>

  <!-- channel pins -->
  <g class="channel">
    <polygon class="pin-base-side" points="490,782 554,745 618,782 618,795 554,832 490,795"/>
    <polygon class="pin-base-top" points="490,782 554,745 618,782 554,819"/>
    <ellipse class="pin-shadow" cx="554" cy="781" rx="24" ry="8"/>
    <path class="pin" d="M554,780 C530,758 498,735 498,700 A56,56 0 1 1 610,700 C610,735 578,758 554,780 Z"/>
    <text class="pin-text" x="554" y="711">Web</text>
  </g>
  <g class="channel">
    <polygon class="pin-base-side" points="797,903 861,866 925,903 925,916 861,953 797,916"/>
    <polygon class="pin-base-top" points="797,903 861,866 925,903 861,940"/>
    <ellipse class="pin-shadow" cx="861" cy="902" rx="24" ry="8"/>
    <path class="pin" d="M861,901 C837,879 805,856 805,821 A56,56 0 1 1 917,821 C917,856 885,879 861,901 Z"/>
    <text class="pin-text" x="861" y="832">Mail</text>
  </g>
  <g class="channel">
    <polygon class="pin-base-side" points="1107,782 1171,745 1235,782 1235,795 1171,832 1107,795"/>
    <polygon class="pin-base-top" points="1107,782 1171,745 1235,782 1171,819"/>
    <ellipse class="pin-shadow" cx="1171" cy="781" rx="24" ry="8"/>
    <path class="pin" d="M1171,780 C1147,758 1115,735 1115,700 A56,56 0 1 1 1227,700 C1227,735 1195,758 1171,780 Z"/>
    <text class="pin-text" x="1171" y="711">Social</text>
  </g>

  <!-- web targets -->
  <g class="steps">
    <rect class="step-box" x="233" y="956" width="229" height="68"/>
    <text class="step-text" x="242" y="985">Portale im</text>
    <text class="step-text" x="242" y="1014">Medien-Netzwerk</text>
    <rect class="step-box" x="233" y="1080" width="229" height="68"/>
    <text class="step-text" x="242" y="1121">Sucharo &amp; Co.</text>
  </g>

  <!-- mail targets -->
  <g class="steps">
    <rect class="step-box" x="723" y="1010" width="276" height="126"/>
    <text class="step-text" x="732" y="1038">Marketing-Verteiler</text>
    <text class="step-text" x="732" y="1067">Fach-/Führungskräfte,</text>
    <text class="step-text" x="732" y="1096">Entscheider,</text>
    <text class="step-text" x="732" y="1125">Meinungsmacher, ...</text>
    <rect class="step-box" x="723" y="1180" width="276" height="68"/>
    <text class="step-text" x="732" y="1221">Journalisten-Verteiler</text>
    <rect class="step-box" x="723" y="1291" width="276" height="68"/>
    <text class="step-text" x="732" y="1332">Individuelle Verteiler</text>
  </g>

  <!-- social targets -->
  <g class="steps">
    <rect class="step-box" x="1260" y="905" width="229" height="68"/>
    <text class="step-text" x="1268" y="946">Freundeskreis</text>
    <rect class="step-box" x="1260" y="1019" width="229" height="68"/>
    <text class="step-text" x="1268" y="1060">Zwitschernetz</text>
    <rect class="step-box" x="1260" y="1131" width="229" height="68"/>
    <text class="step-text" x="1268" y="1172">Berufsprofil</text>
  </g>

  <!-- audience platform -->
  <g class="audience">
    <polygon class="audience-side" points="424,1495 520,1440 1215,1440 1310,1495 1310,1510 1215,1565 520,1565 424,1510"/>
    <polygon class="audience-top" points="424,1495 520,1440 1215,1440 1310,1495 1215,1550 520,1550"/>
    <rect class="audience-people" x="515" y="1405" width="700" height="122" rx="30" role="img" aria-label="Illustration: Reihe von Zielgruppen-Personen (Fach- und Führungskräfte, Journalisten)"/>
  </g>

  <!-- diamond: Ihre Firma + claim -->
  <g class="diamond">
    <polygon class="diamond-edge" points="861,1762 1100,1900 861,2038 622,1900"/>
    <text class="claim" x="861" y="1908">EINFACH.  ERFOLGREICH.</text>
    <text class="claim" x="861" y="1944">KUNDEN GEWINNEN.</text>
    <polygon class="diamond-base" points="670,1745 861,1856 1052,1745 1052,1760 861,1871 670,1760"/>
    <polygon class="diamond-edge" points="861,1634 1052,1745 861,1856 670,1745"/>
    <text class="diamond-title" x="861" y="1757">IHRE FIRMA</text>
  </g>
</svg>
</body>
</html>
```